Wellness Coach needs a Business Card

I need a business card for a start-up coaching business called Brightfern Vitality Partners. I don't have a logo as such but I am looking to have a web page created in a few months time and hopefully the person who designs this card will be able to do or help with the web project. This business card will be used primarily for networking and for initial clients.

As the name implies, the coaching focus is wide-ranging and includes multiple facets of health and wellness, including physical, mental, spiritual, etc. I am a Personal Trainer so the main focus will be physical training, but with the other areas of life / wellness included.

My information for the card:

Dorian Pleshey
Director
Brightfern Vitality Partners

Phone: 0413 862051
Address: PO Box 514 Fernvale ACT 2619
email: dorian@brightfernvitalitypartners.com.au
web: http://www.brightfernvitalitypartners.com.au

Target Market(s)

People wanting to change their life by getting fit and by addressing issues in their lives that are holding them back. I will target people already into fitness but who want to extend their approach into life coaching.

Industry/Entity Type

Health

Requirements
Must have
• - I am keen on a single sided business card design but if your design lends itself to a double sided design then I'm open to that thanks.

- I love the idea of fresh - something that represents the awakening of somebody who has been dormant. Lime green strikes me as fresh, but this is just an idea, not mandatory.
Nice to have
• - I'm keen for minimisation but I don't mind an image in the background taking up the whole space, as long as it is not too busy.

- Two types of images that I can visualise are a mountain summit or a path leading into nature or up a mountain - an adventure! Again, not mandatory, just an idea.
Should not have
• - I'm not keen on over-crowding.
- One image I'm not keen on is someone standing on top of a mountain with their arms in the air - too cliché.

```html
<!DOCTYPE html>
<html lang="en">
<head>
<meta charset="utf-8">
<title>Dorian Pleshey – Brightfern Vitality Partners</title>
<link rel="stylesheet" href="https://fonts.googleapis.com/css2?family=Federo&family=Italiana&family=Poiret+One&display=swap">
<style>
  :root {
    --plum: #5d0c58;
    --ink: #231a24;
    --lime: #b5e619;
    --lime-soft: #e8f5c4;
    --paper: #ffffff;
  }
  * { margin: 0; padding: 0; box-sizing: border-box; }
  html, body {
    width: 1200px;
    height: 777px;
    overflow: hidden;
    background: var(--paper);
  }
  .card {
    position: relative;
    width: 1200px;
    height: 777px;
    background: var(--paper);
    color: var(--ink);
  }
  .line {
    position: absolute;
    left: 0;
    right: 0;
    text-align: center;
    line-height: 1;
    white-space: nowrap;
    font-weight: 400;
  }
  .brand-mark {
    position: absolute;
    left: 600px;
    top: 153px;
    width: 0;
    height: 0;
  }
  .brand-mark svg {
    position: absolute;
    left: -140px;
    top: -140px;
  }
  .brand-name {
    position: absolute;
    left: -120px;
    top: -34px;
    width: 240px;
    text-align: center;
    font-family: "Italiana", serif;
    font-size: 27px;
    line-height: 1.25;
    color: var(--plum);
  }
  .person-name {
    top: 308px;
    font-family: "Federo", sans-serif;
    font-size: 68px;
    color: var(--plum);
    letter-spacing: 1px;
    text-transform: uppercase;
  }
  .person-role {
    top: 388px;
    font-family: "Poiret One", sans-serif;
    font-size: 36px;
    color: var(--ink);
    text-transform: uppercase;
  }
  .company-name {
    top: 452px;
    font-family: "Italiana", serif;
    font-size: 68px;
    color: var(--plum);
    letter-spacing: 1px;
    text-transform: uppercase;
  }
  .phone {
    top: 560px;
    font-family: "Poiret One", sans-serif;
    font-size: 38px;
  }
  .address {
    top: 652px;
    font-family: "Poiret One", sans-serif;
    font-size: 38px;
  }
  .web-links {
    top: 710px;
    font-family: "Poiret One", sans-serif;
    font-size: 34px;
  }
  .web-links .divider {
    color: var(--lime);
    padding: 0 6px;
  }
</style>
</head>
<body>
  <main class="card">
    <div class="brand-mark">
      <svg width="280" height="280" viewBox="0 0 280 280" aria-hidden="true">
        <circle cx="140" cy="140" r="132" fill="none" stroke="var(--lime-soft)" stroke-width="6"/>
      </svg>
      <p class="brand-name">Brightfern<br>Vitality<br>Partners</p>
    </div>

    <h1 class="line person-name">Dorian Pleshey</h1>
    <p class="line person-role">Director</p>
    <p class="line company-name">Brightfern Vitality Partners</p>

    <p class="line phone">0413 862051</p>
    <p class="line address">PO Box 514 Fernvale ACT 2619</p>
    <p class="line web-links">dorian@brightfernvitalitypartners.com.au<span class="divider">|</span>www.brightfernvitalitypartners.com.au</p>
  </main>
</body>
</html>
```